Flaschenetikett Jörgi`s ColaMix
Zielgruppe
Wir machen einen ColaMix, weil wir es können und ihm eine Prise 80er verpassen wollen.
Hip, Trendig und ein bisschen Oldschool.
Bei uns kommt nur in die Flasche, was uns selber schmeckt und dabei preislich fair ist! Kein Schnickschnack, dafür mit viel Geschmack und einer Portion Oldschool.
Einfach einen richtig guten Brauso ähhmm, ColaMix!
Farben:
orange / weiss (Hintergrund Orange & Schrift Weiss)
oder
weiss / anthrazit
Flaschenfarbe:
braun
Etikettgröße:
max. 10 x 10 cm
Name:
Jörgis ColaMix
Zusatztext:
MÜNCHEN
ColaMix (muss irgendwo auf dem Etikett stehen)
Die Beispiele finden wir ultra hip, ein bisschen oldschool, trendig und genau richtig. Alles simpel, kein BlimBlim aber dafür einen ziemlich hohen Stylfaktor.
Wir sind nicht modern, sondern Kinder der 80iger, stehen auf Industrie Vintage Zeug und brauchen einen "ColaMix" der zu uns passt.
Jörg, ja einfach Jörg soll er heissen. Ein deutscher Trendname aus dem 19.Jahrhundert und doch jung und frisch! Genau wie unser ColaMix.
Das Kultgetränk das Allen schmeckt kommt in einer Oldschool braunen Flasche um die Ecke.
WIR MACHEN UNS FAST IN DIE HOSEN VOR AUFREGUNG, WAS IHR SO AUF DER FLASCHE HABT!!!!
HAUT REIN!!!

```html
<!DOCTYPE html>
<html lang="de">
<head>
<meta charset="utf-8">
<title>Jörgis ColaMix – Flaschenetikett</title>
<link rel="stylesheet" href="https://fonts.googleapis.com/css2?family=Oswald:wght@400;500&family=Montserrat:wght@600;700&display=swap">
<style>
  :root {
    --paper: #ffffff;
    --ink: #1d1d1b;
    --anthracite: #58585a;
    --frame-grey: #6d6e70;
    --ribbon-tail: #9d9d9f;
    --ray: #e6e6e7;
    --orange: #f28a1e;
  }
  * { margin: 0; padding: 0; box-sizing: border-box; }
  html, body {
    width: 1200px;
    height: 900px;
    overflow: hidden;
    background: var(--paper);
  }
  .canvas {
    position: relative;
    width: 1200px;
    height: 900px;
  }
  .bottle-label {
    position: absolute;
    left: 339px;
    top: 176px;
    width: 519px;
    height: 519px;
  }
  .bottle-label svg { display: block; }
  .since-line {
    font-family: "Montserrat", sans-serif;
    font-weight: 700;
    font-size: 15px;
    letter-spacing: 3px;
    fill: var(--ink);
  }
  .brand-name {
    font-family: "Oswald", sans-serif;
    font-weight: 500;
    font-size: 66px;
    fill: var(--anthracite);
  }
  .product-name {
    font-family: "Oswald", sans-serif;
    font-weight: 500;
    font-size: 118px;
    fill: var(--orange);
  }
  .banner-text {
    font-family: "Oswald", sans-serif;
    font-weight: 400;
    font-size: 17px;
    letter-spacing: 3.2px;
    fill: var(--paper);
  }
  .volume {
    font-family: "Oswald", sans-serif;
    font-weight: 400;
    font-size: 19px;
    fill: var(--anthracite);
  }
  .legal-note {
    font-family: "Montserrat", sans-serif;
    font-weight: 600;
    font-size: 8.2px;
    fill: var(--orange);
  }
</style>
</head>
<body>
<main class="canvas">
  <section class="bottle-label" aria-label="Flaschenetikett Jörgis ColaMix">
    <svg width="519" height="519" viewBox="0 0 519 519">
      <defs>
        <radialGradient id="sunburst-tone" cx="50%" cy="50%" r="50%">
          <stop offset="0%" stop-color="var(--ray)" stop-opacity="1"/>
          <stop offset="65%" stop-color="var(--ray)" stop-opacity="0.7"/>
          <stop offset="100%" stop-color="var(--ray)" stop-opacity="0"/>
        </radialGradient>
      </defs>

      <rect class="outer-frame" x="1.5" y="1.5" width="516" height="516" fill="var(--paper)" stroke="var(--ink)" stroke-width="3"/>
      <rect class="inner-frame" x="12" y="12" width="495" height="495" fill="none" stroke="var(--frame-grey)" stroke-width="3.5"/>

      <circle class="sunburst" role="img" aria-label="Strahlenkranz hinter dem Namen" cx="259" cy="250" r="200" fill="url(#sunburst-tone)"/>

      <path class="brand-tab" d="M232 0 H286 V66 A27 27 0 0 1 232 66 Z" fill="var(--orange)"/>
      <circle class="brand-dot" cx="259" cy="55" r="16" fill="none" stroke="var(--paper)" stroke-width="3"/>

      <text class="since-line" text-anchor="middle" transform="translate(197 60) rotate(-13)">SINCE</text>
      <text class="since-line" text-anchor="middle" transform="translate(322 60) rotate(13)">2016</text>

      <text class="brand-name" x="259" y="178" text-anchor="middle" textLength="122" lengthAdjust="spacingAndGlyphs">JÖRGS</text>

      <text class="product-name" x="259" y="340" text-anchor="middle" textLength="370" lengthAdjust="spacingAndGlyphs">ColaMix</text>

      <rect class="skyline" role="img" aria-label="Silhouette der Münchner Stadtsilhouette mit Riesenrad, Frauenkirche, Fernsehturm, Stadion und Windrad" x="191" y="392" width="164" height="34" fill="var(--anthracite)" opacity="0.85"/>

      <path class="ribbon-tail" d="M112 442 H145 V480 H112 L122 461 Z" fill="var(--ribbon-tail)"/>
      <path class="ribbon-tail" d="M405 442 H372 V480 H405 L395 461 Z" fill="var(--ribbon-tail)"/>
      <rect class="ribbon" x="138" y="432" width="241" height="38" fill="var(--frame-grey)"/>
      <text class="banner-text" x="258.5" y="457" text-anchor="middle">MADE FOR MUNICH</text>

      <text class="volume" transform="translate(40 498) rotate(-90)">0,5 L</text>

      <text class="legal-note" transform="translate(499 498) rotate(-90)">COFFEINHALTIGES MIXGETRÄNK</text>
    </svg>
  </section>
</main>
</body>
</html>
```